Global Nano Technology Surface Protection company needs a new logo and cards

We are a Global company that will apply nanotechnology coatings on surfaces to prevent growth and spread of bacteria, viruses, mold etc. We deal with large corporates, airlines, hospitals and schools so we are after a new modern, simple and clean look that will have great visual impact.
We a company that is focused on prevention and protection.

Company name, Quorvane Systems Worldwide

Subtext, Antimicrobial Surface Protection

Logo, QVSW or QSW

Target Market(s)

Hospitals, Transport agencies, Airlines, Corporate entities

Industry/Entity Type

Protection

Contact Information for Business Card

Logo, QVSW or QSW
www.qvsw-example.us
Derek Holloway
+64290536218
tidyshieldnz@mailbox-example.com

Logo Text

QVSW

Requirements
Must have
• Simple clean look
Should not have
• Nothing too messy

```html
<!DOCTYPE html>
<html lang="en">
<head>
<meta charset="utf-8">
<title>Quorvane Systems Worldwide – Business Cards</title>
<link rel="stylesheet" href="https://fonts.googleapis.com/css2?family=Arimo:wght@400;700&display=swap">
<style>
  :root {
    --backdrop: #dcdcdc;
    --card-dark: #414143;
    --card-light: #ffffff;
    --brand-blue: #1f74c4;
    --ink: #3b3b3d;
    --ink-soft: #4a4a4a;
    --map-grey: #e6e6e6;
  }
  * { box-sizing: border-box; margin: 0; padding: 0; }
  html, body { width: 1200px; height: 850px; overflow: hidden; }
  body {
    background: var(--backdrop);
    font-family: "Arimo", Arial, sans-serif;
    display: flex;
    flex-direction: column;
    align-items: center;
    justify-content: center;
    gap: 42px;
  }
  .card {
    width: 620px;
    height: 354px;
    border-radius: 22px;
    position: relative;
    overflow: hidden;
  }
  /* Back */
  .card-back {
    background: radial-gradient(circle at 50% 50%, #505055 0%, var(--card-dark) 55%);
    display: flex;
    align-items: center;
    justify-content: center;
  }
  .wordmark-back {
    color: var(--brand-blue);
    font-weight: 700;
    font-size: 104px;
    letter-spacing: 2px;
  }
  /* Front */
  .card-front { background: var(--card-light); }
  .world-map {
    position: absolute;
    left: 40px;
    top: 40px;
    width: 380px;
    height: 250px;
    background: linear-gradient(160deg, var(--map-grey), #eeeeee);
    border-radius: 40px;
  }
  .front-logo {
    position: absolute;
    right: 42px;
    top: 30px;
    display: flex;
    align-items: center;
    gap: 10px;
  }
  .front-logo .dot {
    width: 16px; height: 16px; border-radius: 50%;
    background: var(--brand-blue);
  }
  .front-logo .wordmark {
    color: var(--ink);
    font-weight: 700;
    font-size: 52px;
    letter-spacing: 1px;
  }
  .rule {
    position: absolute;
    left: 230px;
    right: 40px;
    top: 128px;
    height: 1.5px;
    background: var(--brand-blue);
  }
  .company {
    position: absolute;
    right: 40px;
    top: 138px;
    text-align: right;
    color: var(--brand-blue);
    line-height: 1.15;
  }
  .company .line1 { font-weight: 700; font-size: 17px; }
  .company .line2 { font-size: 20px; }
  .tagline {
    position: absolute;
    right: 40px;
    top: 200px;
    text-align: right;
    color: var(--ink-soft);
    font-size: 19px;
    line-height: 1.2;
  }
  .person {
    position: absolute;
    left: 40px;
    top: 108px;
  }
  .person .name {
    color: var(--brand-blue);
    font-weight: 700;
    font-size: 24px;
  }
  .person .role { color: var(--ink-soft); font-size: 15px; margin-top: 2px; }
  .contacts {
    position: absolute;
    left: 40px;
    bottom: 34px;
    list-style: none;
    color: var(--ink);
    font-size: 15px;
  }
  .contacts li { display: flex; align-items: center; gap: 10px; margin-top: 8px; }
  .contacts svg { width: 20px; height: 20px; flex: none; }
</style>
</head>
<body>
  <section class="card card-back" aria-label="Card back">
    <span class="wordmark-back">QVSW</span>
  </section>

  <section class="card card-front" aria-label="Card front">
    <div class="world-map" role="img" aria-label="Faint world map in light grey"></div>

    <div class="front-logo">
      <span class="dot"></span>
      <span class="wordmark">QVSW</span>
    </div>

    <div class="rule"></div>

    <div class="company">
      <div class="line1">Quorvane Systems</div>
      <div class="line2">Worldwide</div>
    </div>

    <div class="tagline">Antimicrobial<br>Surface Protection</div>

    <div class="person">
      <div class="name">Derek Holloway</div>
      <div class="role">managing director</div>
    </div>

    <ul class="contacts">
      <li>
        <svg viewBox="0 0 20 20" aria-hidden="true"><circle cx="10" cy="10" r="9" fill="none" stroke="#1f74c4" stroke-width="1.6"/><path d="M6 7.5c0-1 1-1.5 1.5-1.5l1 2-1 1c.6 1.3 1.4 2.1 2.7 2.7l1-1 2 1c0 .5-.5 1.5-1.5 1.5C8.5 13.2 6 10.7 6 7.5z" fill="#1f74c4"/></svg>
        +64290536218
      </li>
      <li>
        <svg viewBox="0 0 20 20" aria-hidden="true"><circle cx="10" cy="10" r="9" fill="none" stroke="#1f74c4" stroke-width="1.6"/><rect x="5.5" y="7" width="9" height="6.5" fill="none" stroke="#1f74c4" stroke-width="1.3"/><path d="M5.5 7l4.5 3.5L14.5 7" fill="none" stroke="#1f74c4" stroke-width="1.3"/></svg>
        tidyshieldnz@mailbox-example.com
      </li>
      <li>
        <svg viewBox="0 0 20 20" aria-hidden="true"><circle cx="10" cy="10" r="9" fill="none" stroke="#1f74c4" stroke-width="1.6"/><circle cx="10" cy="10" r="5" fill="none" stroke="#1f74c4" stroke-width="1.2"/><path d="M5 10h10M10 5c-2.5 3-2.5 7 0 10M10 5c2.5 3 2.5 7 0 10" fill="none" stroke="#1f74c4" stroke-width="1.1"/></svg>
        www.qvsw-example.us
      </li>
    </ul>
  </section>
</body>
</html>
```